Moravel Stenwick Inc needs a business card design

Looking for a unique, classy and sharp business card design.

Contact Information for Business Card

Moravel Stenwick Inc.
Marisa Ortega Bellido BScOT(c)
Occupational Therapist
(780) 555-0142
moravelstenwick@postlynx.net

```html
<!DOCTYPE html>
<html lang="en">
<head>
<meta charset="utf-8">
<title>Moravel Stenwick Inc. – Business Card</title>
<link href="https://fonts.googleapis.com/css2?family=Source+Sans+3:wght@400;600;700&display=swap" rel="stylesheet">
<style>
  :root {
    --bg: #2e2e30;
    --card-black: #1c1c1e;
    --sky: #29b3e6;
    --lime: #8cc63f;
    --violet: #a23aa8;
    --ink: #1a1a1a;
    --white: #ffffff;
  }
  * { margin: 0; padding: 0; box-sizing: border-box; }
  html, body { width: 1200px; height: 960px; overflow: hidden; }
  body {
    background: var(--bg);
    font-family: "Source Sans 3", "Helvetica Neue", Arial, sans-serif;
    position: relative;
  }
  .card {
    position: absolute;
    width: 620px;
    height: 354px;
    border-radius: 18px;
    overflow: hidden;
    background: var(--card-black);
    box-shadow: 0 18px 40px rgba(0,0,0,.45);
  }
  .card-back { left: 70px; top: 80px; }
  .card-front { left: 510px; top: 520px; }

  .brand {
    display: flex;
    align-items: center;
    gap: 12px;
  }
  .brand-dot {
    width: 22px; height: 22px;
    border-radius: 50%;
    background: var(--lime);
    flex: none;
  }
  .brand-name {
    font-weight: 700;
    font-size: 40px;
    color: var(--violet);
    letter-spacing: .5px;
    line-height: 1;
    white-space: nowrap;
  }
  .card-back .brand {
    position: absolute;
    left: 0; right: 0; top: 130px;
    justify-content: center;
  }
  .website-line {
    position: absolute;
    left: 0; right: 0; top: 262px;
    text-align: center;
    color: var(--white);
    font-size: 15px;
    letter-spacing: 6px;
  }

  .wave { position: absolute; inset: 0; }
  .card-front .brand {
    position: absolute;
    left: 28px; top: 112px;
    gap: 9px;
  }
  .card-front .brand-dot { width: 16px; height: 16px; }
  .card-front .brand-name { font-size: 24px; }

  .contact {
    position: absolute;
    right: 26px; top: 92px;
    text-align: right;
    color: var(--ink);
    line-height: 1.25;
  }
  .contact-name { color: var(--lime); font-weight: 600; font-size: 17px; white-space: nowrap; }
  .contact-title { font-weight: 600; font-size: 16px; }
  .contact-company { font-size: 15px; margin-bottom: 16px; }
  .contact-row {
    font-size: 14px;
    display: flex;
    justify-content: flex-end;
    align-items: center;
    gap: 8px;
    white-space: nowrap;
  }
  .contact-row svg { width: 13px; height: 13px; fill: var(--ink); flex: none; }
</style>
</head>
<body>

<section class="card card-back" aria-label="Card back">
  <div class="brand">
    <span class="brand-dot"></span>
    <span class="brand-name">Moravel Stenwick</span>
  </div>
  <p class="website-line">www.moravelstenwick.com</p>
</section>

<section class="card card-front" aria-label="Card front">
  <svg class="wave" viewBox="0 0 620 354" preserveAspectRatio="none" aria-hidden="true">
    <path fill="var(--violet)" d="M360 0 C300 30 290 140 260 200 C220 280 110 320 -20 330 L-20 354 L620 354 L620 0 Z"/>
    <path fill="var(--lime)" d="M372 0 C312 30 302 142 272 202 C232 284 122 324 -10 334 L-10 354 L620 354 L620 0 Z"/>
    <path fill="var(--sky)" d="M384 0 C324 30 314 144 284 204 C244 288 134 328 0 338 L0 354 L620 354 L620 0 Z"/>
  </svg>

  <div class="brand">
    <span class="brand-dot"></span>
    <span class="brand-name">Moravel Stenwick</span>
  </div>

  <div class="contact">
    <p class="contact-name">Marisa Ortega Bellido BScOT(c)</p>
    <p class="contact-title">Occupational Therapist</p>
    <p class="contact-company">Moravel Stenwick Inc.</p>
    <p class="contact-row">(780) 555-0142
      <svg viewBox="0 0 24 24"><path d="M6.6 10.8a15 15 0 0 0 6.6 6.6l2.2-2.2c.3-.3.7-.4 1-.2 1.1.4 2.3.6 3.6.6.6 0 1 .4 1 1V20c0 .6-.4 1-1 1A17 17 0 0 1 3 4c0-.6.4-1 1-1h3.5c.6 0 1 .4 1 1 0 1.3.2 2.5.6 3.6.1.3 0 .7-.2 1z"/></svg>
    </p>
    <p class="contact-row">moravelstenwick@postlynx.net
      <svg viewBox="0 0 24 24"><path d="M2 5h20v14H2z M3 6l9 7 9-7" stroke="#29b3e6" stroke-width="1.5"/></svg>
    </p>
    <p class="contact-row">www.moravelstenwick.com
      <svg viewBox="0 0 24 24"><circle cx="12" cy="12" r="10"/><path d="M2 12h20M12 2c3 3 3 17 0 20M12 2c-3 3-3 17 0 20" stroke="#29b3e6" stroke-width="1.4" fill="none"/></svg>
    </p>
  </div>
</section>

</body>
</html>
```